Business Cards

I'd like help creating business cards with the full logo "Velmora Capital Partners" on the back of the card (navy background with white writing), and abbreviated logo "VCP" on the front. Would like to list name, title, phone number, email, and website listed on front of card. Would like to keep very simple. Front font Arial or similar.

```html
<!DOCTYPE html>
<html lang="en">
<head>
<meta charset="utf-8">
<title>Velmora Capital Partners – Business Cards</title>
<link href="https://fonts.googleapis.com/css2?family=Open+Sans:wght@400;700&display=swap" rel="stylesheet">
<style>
  :root {
    --backdrop: #d2d2d2;
    --paper: #efefed;
    --navy: #1d3a7a;
    --white: #ffffff;
    --ink-grey: #8a8a8a;
    --rule: #2a4a8a;
  }
  * { box-sizing: border-box; margin: 0; padding: 0; }
  html, body {
    width: 1200px; height: 1051px; overflow: hidden;
    background: var(--backdrop);
    font-family: "Open Sans", Arial, sans-serif;
  }
  .stage { position: relative; width: 1200px; height: 1051px; }
  .card {
    position: absolute;
    width: 520px; height: 297px;
  }
  .card--front {
    left: 40px; top: 377px;
    background: var(--paper);
    border-bottom: 3px solid var(--navy);
  }
  .card--back {
    left: 640px; top: 377px;
    background: var(--navy);
  }

  .monogram {
    position: absolute; left: 34px; top: 30px;
    display: flex; align-items: center; gap: 10px;
  }
  .monogram__square { width: 14px; height: 14px; background: var(--navy); }
  .monogram__name {
    font-size: 38px; font-weight: 700; color: var(--navy); letter-spacing: 1px;
  }

  .divider {
    position: absolute; left: 34px; right: 34px; top: 168px;
    height: 1px; background: var(--rule);
  }
  .holder {
    position: absolute; right: 34px; top: 112px; text-align: right;
  }
  .holder__name {
    font-size: 19px; font-weight: 700; color: var(--navy); letter-spacing: .3px;
  }
  .holder__title { font-size: 13px; color: var(--ink-grey); margin-top: 1px; }

  .contacts {
    position: absolute; left: 34px; top: 188px;
    list-style: none; font-size: 13px; color: var(--ink-grey); line-height: 22px;
  }
  .contacts li { display: flex; align-items: center; gap: 9px; }
  .contacts svg { width: 11px; height: 11px; fill: var(--navy); flex: none; }

  .wordmark {
    position: absolute; inset: 0;
    display: flex; flex-direction: column; align-items: center; justify-content: center;
    color: var(--white); font-weight: 700;
  }
  .wordmark__main { font-size: 44px; letter-spacing: 3px; line-height: 1; }
  .wordmark__sub { font-size: 15px; letter-spacing: 9px; margin-top: 10px; padding-left: 9px; }
</style>
</head>
<body>
<main class="stage">
  <section class="card card--front" aria-label="Business card front">
    <div class="monogram">
      <span class="monogram__square"></span>
      <span class="monogram__name">VCP</span>
    </div>
    <div class="holder">
      <p class="holder__name">DANA WHITCOMBE</p>
      <p class="holder__title">Co-Founder and Managing Partner</p>
    </div>
    <div class="divider"></div>
    <ul class="contacts">
      <li>
        <svg viewBox="0 0 24 24" aria-hidden="true"><path d="M6.6 10.8a15.1 15.1 0 0 0 6.6 6.6l2.2-2.2a1 1 0 0 1 1-.25 11.4 11.4 0 0 0 3.6.57 1 1 0 0 1 1 1V20a1 1 0 0 1-1 1A17 17 0 0 1 3 4a1 1 0 0 1 1-1h3.5a1 1 0 0 1 1 1c0 1.25.2 2.45.57 3.57a1 1 0 0 1-.25 1z"/></svg>
        (555) 204-7310
      </li>
      <li>
        <svg viewBox="0 0 24 24" aria-hidden="true"><path d="M2 5h20v14H2zm2 2v.5l8 5 8-5V7z"/></svg>
        Dana.Whitcombe@VelmoraCP.com
      </li>
      <li>
        <svg viewBox="0 0 24 24" aria-hidden="true"><circle cx="12" cy="12" r="10"/></svg>
        www.velmoracp.com
      </li>
    </ul>
  </section>

  <section class="card card--back" aria-label="Business card back">
    <div class="wordmark">
      <span class="wordmark__main">VELMORA</span>
      <span class="wordmark__sub">CAPITAL PARTNERS</span>
    </div>
  </section>
</main>
</body>
</html>
```